Business Card Design

IT Solutions company.

I need a professional looking design with my company logo if possible.

Logo is located here:
http://www.brivelnetworks.co.uk/dev/images/logo1.jpg
Feel free to redesign the logo if you think you have any better suggestions.

Our services include, IT Infrastructure/Telephony Maintenance & Hosting Services. Linux and Windows Solutions, App Development.

Out website is currently under development:
http://www.brivelnetworks.co.uk/dev/

I'm looking for a colourful but professional looking business card.

Industry/Entity Type

Business

Contact Information for Business Card

Brivel Networks Ltd
Simon Dellaway
07836552918
www.brivelnetworks.co.uk
sdellaway@brivelnetworks.co.uk

```html
<!DOCTYPE html>
<html lang="en">
<head>
<meta charset="utf-8">
<title>Brivel Networks Ltd – Business Card</title>
<link rel="stylesheet" href="https://fonts.googleapis.com/css2?family=Tinos:wght@400&display=swap">
<style>
  :root {
    --page: #ffffff;
    --card: #2a2c34;
    --card-edge: #1e1f25;
    --cream: #f2f0e4;
    --stripe-blue: #1d4590;
    --stripe-grey: #6b6b6b;
    --mark: #44464e;
    --ink: #f4f4f4;
  }
  * { margin: 0; padding: 0; box-sizing: border-box; }
  html, body {
    width: 1200px;
    height: 695px;
    overflow: hidden;
    background: var(--page);
  }
  .card {
    position: absolute;
    left: 45px;
    top: 43px;
    width: 1108px;
    height: 608px;
    background: var(--card);
    border: 2px solid var(--card-edge);
    overflow: hidden;
    font-family: "Tinos", "Times New Roman", serif;
  }
  .card__stripes {
    position: absolute;
    inset: 0;
    width: 100%;
    height: 100%;
  }
  .brand {
    position: absolute;
    left: 268px;
    top: 60px;
    display: flex;
    align-items: center;
    gap: 26px;
    color: var(--mark);
  }
  .brand__ring {
    width: 170px;
    height: 170px;
    border-radius: 50%;
    border: 11px solid var(--mark);
    flex: none;
  }
  .brand__name {
    font-size: 58px;
    font-weight: 400;
    letter-spacing: 0.5px;
    white-space: nowrap;
  }
  .contact {
    position: absolute;
    left: 316px;
    top: 305px;
    list-style: none;
    color: var(--ink);
    font-size: 32px;
    line-height: 52px;
  }
  .contact__row { display: flex; }
  .contact__label { width: 77px; }
</style>
</head>
<body>
  <section class="card">
    <svg class="card__stripes" viewBox="0 0 1108 608" preserveAspectRatio="none" aria-hidden="true">
      <polygon points="0,0 212,0 6,608 0,608" fill="var(--cream)"/>
      <polygon points="212,0 246,0 36,608 6,608" fill="var(--stripe-blue)"/>
      <polygon points="246,0 278,0 68,608 36,608" fill="var(--stripe-grey)"/>
    </svg>

    <div class="brand">
      <span class="brand__ring"></span>
      <span class="brand__name">Brivel Networks Ltd</span>
    </div>

    <ul class="contact">
      <li class="contact__row"><span class="contact__label">N</span><span>&nbsp;Simon Dellaway</span></li>
      <li class="contact__row"><span class="contact__label">A</span><span>07836552918</span></li>
      <li class="contact__row"><span class="contact__label">E</span><span>www.brivelnetworks.co.uk</span></li>
      <li class="contact__row"><span class="contact__label">W</span><span>sdellaway@brivelnetworks.co.uk</span></li>
    </ul>
  </section>
</body>
</html>
```